App UI Design: Shopping/E-commerce App

Project :
Develop an UI design & App icon for an E-commerce/Shopping App

About the App/ Target Audience:
This grocery & food shopping app will be used by independent pub, café, restaurant owners to place & manage their purchases of foods and groceries for their catering businesses.

They will use the app to access product catalogues & special promotions, search & buy large quantities of groceries or catering supplies, and the ability to manage and track status of their order.

The HTML5 App’s has been built with a very basic structure. It now needs the visual layer of the UI designed

Note:
The app is tailored for business & catering orders, not retail/supermarket buyers, so the visual needs to look smart & not too casual.

Reason: Current submissions have not met out expectations. Please use the similar app examples in the PDF as a strong point of reference for the look & feel. Feedback will be given as submissions come in, please feel free to submit initial concepts of 1 or 2 of the pages & we'll provide feedback on whether it is on the right track or not before you do more work. Current submission will also receive feedback in the next few days. We look forward to new submissions!

Target Market(s)

Male & Female. Independent pub, café, restaurant owners buying for their catering businesses. Chefs etc.

Industry/Entity Type

Restaurant

Requirements
Must have
• An overview of elements/pages of the app that needs to be designed are:
(DOWNLOAD a more detailed diagram PDF explanation)

1. Welcome- Log-in Page
2. Homepage – index that links to different function of the app

Products:
3. Promotions page – for products on special for a limited time
4. Catalogue page – access to a range of catalogue

Ways to buy:
5. Basket (Shopping Cart) - tracking items they are buying from the catalogues
6. Templates (Pre-set Shopping list)- Set shopping list that has been preloaded for certain menu
7. Open Order page

My Account:
8. My Account/profile page – Users can check the status of their order, look at past orders, look at their account number & details etc

_______________________________________________________

Icon set- Icons to represent each pages that act as visual cues for easier browsing.

2 Main features that need to be accessible & consistent throughout all pages are:
a) The Navigation Bar –
so the user can quickly find their way back & access to the main functions
b) The Search bar –
whether it drops down when needed, or is featured as a header/footer.
c) Log out button
Nice to have
• _______________________________________________________

Things to keep in mind:

The UI design essentially needs to be a customizable template that can easily adapt to any brand/logo with a slight change of the color scheme. As we will later implement our brand & logo onto it.

We’re looking for a clean & clear design that allows for a straight forward easy user experience.

You are free to develop different layout & UI pattern that you feel is the most efficient way the user can walk through the App & make their purchase in no more than 2 or 3 clicks
________________________________________________

Screenshot of Similar Apps for reference are also in the PDF

```html
<!DOCTYPE html>
<html lang="en">
<head>
<meta charset="utf-8">
<title>Home</title>
<link rel="stylesheet" href="https://fonts.googleapis.com/css2?family=Arimo:wght@400;700&display=swap">
<style>
  :root {
    --status-bg: #000000;
    --status-text: #ffffff;
    --header-top: #c3cbd0;
    --header-bottom: #8f9ba5;
    --page-bg: #eeedeb;
    --field-bg: #ffffff;
    --field-border: #7d8890;
    --placeholder: #a9adb0;
    --icon: #8893a1;
    --label: #434a52;
    --rule: #c2c7cc;
    --rule-light: #ffffff;
    --button-top: #cfd6da;
    --button-bottom: #7f8b95;
    --button-text: #ffffff;
  }
  * { box-sizing: border-box; margin: 0; padding: 0; }
  html, body {
    width: 800px; height: 1200px; overflow: hidden;
    background: var(--page-bg);
    font-family: "Arimo", Helvetica, Arial, sans-serif;
  }
  .screen { position: relative; width: 800px; height: 1200px; background: var(--page-bg); }

  .status-bar {
    position: absolute; top: 0; left: 0; width: 800px; height: 50px;
    background: var(--status-bg); color: var(--status-text);
    font-weight: 700; font-size: 27px;
  }
  .status-bar .carrier { position: absolute; left: 10px; top: 9px; display: flex; align-items: flex-end; gap: 8px; }
  .signal { display: flex; align-items: flex-end; gap: 3px; height: 26px; padding-bottom: 3px; }
  .signal span { width: 5px; background: var(--status-text); }
  .status-bar .time { position: absolute; left: 0; right: 0; top: 9px; text-align: center; }
  .status-bar .tray { position: absolute; right: 14px; top: 11px; display: flex; gap: 16px; align-items: center; }

  .nav-header {
    position: absolute; top: 50px; left: 0; width: 800px; height: 219px;
    background: linear-gradient(var(--header-top), var(--header-bottom));
    border-bottom: 1px solid #7a858e;
  }
  .nav-header h1 {
    position: absolute; top: 26px; width: 100%; text-align: center;
    font-size: 47px; font-weight: 700; color: #fff;
    text-shadow: 0 -1px 1px rgba(60,70,80,.5);
  }
  .search-field {
    position: absolute; top: 129px; left: 13px; width: 775px; height: 71px;
    background: var(--field-bg); border: 2px solid var(--field-border); border-radius: 36px;
    box-shadow: inset 0 3px 4px rgba(0,0,0,.25), 0 1px 0 rgba(255,255,255,.5);
    display: flex; align-items: center; padding-left: 22px; gap: 18px;
  }
  .search-field .placeholder { font-size: 35px; font-weight: 700; color: var(--placeholder); }

  .menu-grid {
    position: absolute; top: 318px; left: 0; width: 800px; height: 679px;
    border-top: 2px solid var(--rule);
    display: grid; grid-template-columns: 404px 396px; grid-template-rows: repeat(3, 225px);
  }
  .menu-item {
    position: relative; display: block; text-decoration: none;
    border-bottom: 2px solid var(--rule);
    box-shadow: inset 0 2px 0 var(--rule-light);
  }
  .menu-item:nth-child(odd) { border-right: 2px solid var(--rule); }
  .menu-item:nth-child(even) { box-shadow: inset 0 2px 0 var(--rule-light), inset 2px 0 0 var(--rule-light); }
  .menu-item svg { position: absolute; left: 50%; top: 28px; width: 130px; height: 130px; transform: translateX(-50%); fill: var(--icon); }
  .menu-item .label {
    position: absolute; left: 0; right: 0; top: 166px; text-align: center;
    font-size: 27px; font-weight: 700; color: var(--label);
    text-shadow: 0 1px 0 #fff;
  }

  .sign-out {
    position: absolute; left: 240px; top: 1107px; width: 320px; height: 76px;
    border-radius: 8px; border: 2px solid #e4e7ea;
    background: linear-gradient(var(--button-top), var(--button-bottom));
    color: var(--button-text); font-family: inherit; font-weight: 700; font-size: 27px;
    text-shadow: 0 -1px 1px rgba(50,60,70,.5);
    box-shadow: 0 1px 3px rgba(0,0,0,.3);
  }
</style>
</head>
<body>
<div class="screen">

  <div class="status-bar">
    <div class="carrier">
      <div class="signal"><span style="height:8px"></span><span style="height:12px"></span><span style="height:16px"></span><span style="height:20px"></span><span style="height:24px"></span></div>
      <span>Carrio</span>
    </div>
    <div class="time">10:20 PM</div>
    <div class="tray">
      <svg width="26" height="26" viewBox="0 0 26 26"><circle cx="13" cy="13" r="12" fill="#fff"/><path d="M13 6v8h5" stroke="#000" stroke-width="3" fill="none"/></svg>
      <svg width="48" height="26" viewBox="0 0 48 26"><rect x="1.5" y="2.5" width="41" height="21" rx="3" fill="none" stroke="#fff" stroke-width="3"/><rect x="5" y="6" width="34" height="14" fill="#fff"/><rect x="43" y="9" width="4" height="8" fill="#fff"/></svg>
    </div>
  </div>

  <header class="nav-header">
    <h1>Home</h1>
    <div class="search-field">
      <svg width="36" height="36" viewBox="0 0 36 36"><circle cx="14" cy="14" r="10.5" fill="none" stroke="#7b8288" stroke-width="4.5"/><path d="M22 22l10 10" stroke="#7b8288" stroke-width="5.5" stroke-linecap="round"/></svg>
      <span class="placeholder">Search</span>
    </div>
  </header>

  <nav class="menu-grid">
    <a class="menu-item" href="#promotions">
      <svg viewBox="0 0 100 100"><path d="M40 10c6-4 10 2 9 8l-3 20h33c6 0 9 5 7 9 3 2 3 7 0 9 2 2 2 7-1 9 2 3 0 8-4 8H44c-10 0-18-3-20-8-3-8-2-20 3-27 6-8 11-15 13-28z"/></svg>
      <span class="label">Promotions</span>
    </a>
    <a class="menu-item" href="#catalogue">
      <svg viewBox="0 0 100 100"><rect x="30" y="4" width="64" height="86" rx="3" fill="#6f7a88"/><rect x="26" y="2" width="64" height="86" rx="3"/><g fill="none" stroke="var(--icon)" stroke-width="3.5" stroke-linecap="round"><path d="M34 14H18a4 4 0 0 0 0 8h16M34 30H18a4 4 0 0 0 0 8h16M34 46H18a4 4 0 0 0 0 8h16M34 62H18a4 4 0 0 0 0 8h16"/></g><g fill="none" stroke="#eeedeb" stroke-width="1.5"><path d="M34 14H18a4 4 0 0 0 0 8h16M34 30H18a4 4 0 0 0 0 8h16M34 46H18a4 4 0 0 0 0 8h16M34 62H18a4 4 0 0 0 0 8h16"/></g></svg>
      <span class="label">Catalogue</span>
    </a>
    <a class="menu-item" href="#basket">
      <svg viewBox="0 0 100 100"><g fill="none" stroke="var(--icon)" stroke-width="4" stroke-linejoin="round"><path d="M2 18h12l8 50h60"/><path d="M12 18l76-6-6 46H20"/><path d="M34 16l2 42M52 15l1 43M70 13l-2 45M16 32l70-4M18 45l66-3"/></g><circle cx="28" cy="80" r="7"/><circle cx="72" cy="80" r="9"/></svg>
      <span class="label">Basket</span>
    </a>
    <a class="menu-item" href="#order-template">
      <svg viewBox="0 0 100 100"><path d="M18 12l38-4 12 78-36 6z" fill="#7a8593"/><path d="M30 4h42l12 12v76H30z"/><path d="M72 4v12h12z" fill="#c3cad1"/><g stroke="#eeedeb" stroke-width="4"><path d="M38 30h38M38 40h38M38 50h38M62 68h14"/></g></svg>
      <span class="label">Order Template</span>
    </a>
    <a class="menu-item" href="#open-order">
      <svg viewBox="0 0 100 100"><path d="M20 2h42l16 16v80H20z"/><path d="M62 2v16h16z" fill="#c3cad1"/><g stroke="#eeedeb" stroke-width="4"><path d="M28 32h42M28 44h42M28 56h42"/></g><path d="M52 80l6 6 12-12" stroke="#eeedeb" stroke-width="4" fill="none"/></svg>
      <span class="label">Open Order</span>
    </a>
    <a class="menu-item" href="#my-account">
      <svg viewBox="0 0 100 100"><ellipse cx="50" cy="28" rx="20" ry="24"/><path d="M2 98c0-24 20-38 48-38s48 14 48 38z"/></svg>
      <span class="label">My Account</span>
    </a>
  </nav>

  <button class="sign-out" type="button">Sign Out</button>
</div>
</body>
</html>
```